Korvane Business Cards

We need a business card design. We are a Technology (Audio Visual) design, sales and installation company. Looking for a double sided design, clean

Contact Information for Business Card

Clean, modern look, 2 sided

Font styles to use
Sans Serif

```html
<!DOCTYPE html>
<html lang="en">
<head>
<meta charset="utf-8">
<title>Korvane Business Cards</title>
<link rel="stylesheet" href="https://fonts.googleapis.com/css2?family=Fira+Sans:wght@400;500;600;700&display=swap">
<style>
  :root {
    --ink: #0d1011;
    --paper: #ffffff;
    --accent: #f7931e;
    --text: #111111;
  }
  html, body {
    margin: 0;
    padding: 0;
    width: 966px;
    height: 1200px;
    overflow: hidden;
    background: var(--paper);
    font-family: "Fira Sans", sans-serif;
    font-variant-numeric: oldstyle-nums;
  }
  .canvas {
    position: relative;
    width: 966px;
    height: 1200px;
  }

  /* Front side */
  .card-front {
    position: absolute;
    left: 112px;
    top: 105px;
    width: 749px;
    height: 429px;
    background: var(--ink);
    display: flex;
    align-items: center;
    justify-content: center;
  }
  .brand {
    display: flex;
    align-items: center;
    gap: 14px;
    margin-top: -14px;
  }
  .brand-name {
    font-weight: 700;
    font-size: 76px;
    letter-spacing: -1px;
    color: var(--paper);
    line-height: 1;
  }
  .brand-mark {
    width: 16px;
    height: 16px;
    background: var(--accent);
    margin-top: -36px;
  }

  /* Back side */
  .card-back {
    position: absolute;
    left: 107px;
    top: 666px;
    width: 743px;
    height: 424px;
    background: var(--paper);
    border: 2px solid var(--ink);
    color: var(--text);
  }
  .holder {
    position: absolute;
    right: 20px;
    top: 12px;
    text-align: right;
  }
  .holder-name {
    display: flex;
    align-items: center;
    justify-content: flex-end;
    gap: 14px;
    font-weight: 600;
    font-size: 26px;
    line-height: 1.2;
  }
  .holder-name svg { width: 24px; height: 24px; }
  .holder-role {
    font-size: 18px;
    margin-top: 2px;
    margin-right: 6px;
  }
  .contact {
    position: absolute;
    display: flex;
    align-items: center;
    font-size: 21px;
    letter-spacing: 0.3px;
  }
  .contact svg { width: 22px; height: 26px; }
  .contact .sep { margin: 0 14px 0 10px; }
  .contact-phone { left: 96px; top: 284px; }
  .contact-email { left: 391px; top: 284px; }
  .contact-web { left: 206px; top: 330px; }

  .address-band {
    position: absolute;
    left: 0;
    right: 0;
    bottom: 0;
    height: 52px;
    background: var(--ink);
    color: var(--accent);
    display: flex;
    align-items: center;
    justify-content: center;
    font-size: 21px;
    letter-spacing: 0.3px;
  }
  .address-band svg { width: 24px; height: 22px; }
  .address-band .sep { margin: 0 10px 0 8px; }
</style>
</head>
<body>
<div class="canvas">

  <section class="card-front">
    <div class="brand">
      <span class="brand-name">Korvane</span>
      <span class="brand-mark"></span>
    </div>
  </section>

  <section class="card-back">
    <div class="holder">
      <div class="holder-name">
        <svg viewBox="0 0 24 24" fill="none" stroke="#111" stroke-width="2" stroke-linecap="round">
          <circle cx="13" cy="8" r="5.5"/>
          <path d="M3 22c1-5 4-8 8-8.5"/>
        </svg>
        <span>Daren Holloway</span>
      </div>
      <div class="holder-role">chief executive officer</div>
    </div>

    <div class="contact contact-phone">
      <svg viewBox="0 0 22 26" fill="none" stroke="#111" stroke-width="2">
        <rect x="3" y="2" width="16" height="22" rx="3"/>
        <circle cx="11" cy="20" r="0.8" fill="#111"/>
      </svg>
      <span class="sep">:</span>
      <span>(000)000-123</span>
    </div>

    <div class="contact contact-email">
      <svg viewBox="0 0 26 22" fill="none" stroke="#111" stroke-width="2" style="width:26px;height:22px">
        <path d="M2 4h22v15H8"/>
        <path d="M2 4l11 8 11-8"/>
        <path d="M2 4v10"/>
      </svg>
      <span class="sep">:</span>
      <span>email@your.com</span>
    </div>

    <div class="contact contact-web">
      <svg viewBox="0 0 24 24" fill="none" stroke="#111" stroke-width="2" style="width:24px;height:24px">
        <circle cx="12" cy="12" r="9"/>
        <path d="M3 12h18M12 3v18M8 4c-2 5-2 11 0 16M16 4c2 5 2 11 0 16"/>
      </svg>
      <span class="sep">:</span>
      <span>www.yourcompany.com</span>
    </div>

    <div class="address-band">
      <svg viewBox="0 0 24 22" fill="none" stroke="#f7931e" stroke-width="2" stroke-linejoin="round">
        <path d="M2 11L12 2l10 9"/>
        <path d="M5 9v11M19 9v11"/>
      </svg>
      <span class="sep">:</span>
      <span>Address line 1, Address line 2, Address line 3</span>
    </div>
  </section>

</div>
</body>
</html>
```